Motorcycle Mechanic - Van and Business Card Design

Need a van and business card designed for a company called Gear Mend.

Gearmend is a mobile motorcycle mechanic based in Sydney Australia. The goal of the design is to stand out look modern. The van is Black and generally the designs will be on a darker colour using brighter colours to contrast and grab attention.

Company Colours are slightly off black (background) and yellow, slightly off white.

Really like the designs of energy drink vehicles (https://imgvault.example-host.net/2012/11/vehicle-wrap-sample.jpg?w=1500) and kornwalder (http://blog.quillstudio.example.com.au/uploads/2008/03/utevectorside.jpg) promotional vehicles.

Details on car to include:

Website: gear-mend.com.au
Phone: 9312 5827
Services: Servicing, Repairs, Pickup & Emergency Callouts

*The above on both side panels & rear of van
*If services too hard to fit everything on rear prioritise the logo, phone number and website.

Car is a 2014 Black, Norvik Trava.- See images attached for reference.

Files to be provided in .ai or .eps.

Business card details:

Dimensions: 85mm x 54mm
Bleed: 2mm

Name: Tomas Brandel
Phone: 9312 5827
Email: tomas@gear-mend.com.au

Logo to be included on either both or one side. Base of card should be dark close to black for at least one side (ok for both, designers call).

Target Market(s)

Bike Owners

Industry/Entity Type

Mechanic

Font styles to use
Sans Serif

Requirements
Must have
• Files in .ai or .eps
• Must catch attention without looking tacky.
• Must have details mentioned in the product description.
Nice to have
• Graphical elements that bring attention to important information.
Should not have
• Any non vector imagery. Any clipart of photographic type imagery. Too many colours. Any imagery or graphics that breach trademarks or copyright laws.

```html
<!DOCTYPE html>
<html lang="en">
<head>
<meta charset="utf-8">
<title>Gearmend Business Card</title>
<link rel="stylesheet" href="https://fonts.googleapis.com/css2?family=Montserrat:wght@400;600&family=Roboto:wght@300;400&display=swap">
<style>
  :root {
    --ink: #141414;
    --ink-soft: #1c1c1c;
    --yellow: #ffcc00;
    --offwhite: #f2f2ee;
    --backdrop: #d9d9d7;
  }
  * { box-sizing: border-box; margin: 0; padding: 0; }
  html, body { width: 1200px; height: 1200px; overflow: hidden; }
  body {
    background: var(--backdrop);
    position: relative;
    font-family: "Roboto", Arial, sans-serif;
  }
  .card {
    position: absolute;
    left: 220px;
    width: 760px;
    height: 483px;
    background: linear-gradient(160deg, var(--ink-soft), var(--ink));
    overflow: hidden;
    box-shadow: 0 10px 28px rgba(0,0,0,0.25);
  }
  .card--front { top: 84px; }
  .card--back { top: 633px; }

  /* tabs */
  .tab { position: absolute; }
  .tab--top {
    top: 0; left: 290px; width: 290px; height: 20px;
    background: var(--yellow);
    border-radius: 0 0 6px 6px;
  }
  .tab--right {
    right: 0; top: 130px; width: 20px; height: 190px;
    background: var(--ink);
    border-radius: 6px 0 0 6px;
  }
  .tab--left {
    left: 0; top: 140px; width: 20px; height: 190px;
    background: var(--yellow);
    border-radius: 0 6px 6px 0;
  }

  /* brand lockup */
  .brand {
    position: absolute;
    display: flex;
    align-items: center;
    gap: 18px;
  }
  .brand__mark {
    flex: none;
    border-radius: 50%;
    background: var(--yellow);
  }
  .brand__text { display: flex; flex-direction: column; }
  .brand__name {
    font-family: "Montserrat", Arial, sans-serif;
    font-weight: 400;
    color: var(--offwhite);
    letter-spacing: 0.02em;
    line-height: 1;
  }
  .brand__tagline {
    font-family: "Montserrat", Arial, sans-serif;
    font-weight: 600;
    color: var(--offwhite);
    text-transform: uppercase;
    letter-spacing: 0.04em;
    white-space: nowrap;
  }
  .card--front .brand { left: 150px; top: 200px; }
  .card--front .brand__mark { width: 78px; height: 78px; }
  .card--front .brand__name { font-size: 58px; }
  .card--front .brand__tagline { font-size: 11.5px; margin-top: 6px; }

  /* back */
  .back__dark {
    position: absolute; left: 0; top: 0; width: 380px; height: 100%;
  }
  .back__dark .brand { left: 60px; top: 212px; gap: 12px; }
  .back__dark .brand__mark { width: 44px; height: 44px; }
  .back__dark .brand__name { font-size: 32px; }
  .back__dark .brand__tagline { font-size: 6.4px; margin-top: 4px; }

  .back__light {
    position: absolute; right: 0; top: 0; width: 380px; height: 100%;
    background: var(--yellow);
    padding: 150px 0 0 56px;
    color: var(--ink);
  }
  .contact__name {
    font-size: 40px;
    font-weight: 400;
    margin-bottom: 26px;
  }
  .contact__row {
    display: flex; align-items: center; gap: 16px;
    font-size: 21px; font-weight: 300;
    margin-bottom: 14px;
  }
  .contact__icon { width: 22px; height: 22px; flex: none; }
</style>
</head>
<body>

  <section class="card card--front" aria-label="Business card front">
    <div class="tab tab--top"></div>
    <div class="brand">
      <div class="brand__mark"></div>
      <div class="brand__text">
        <span class="brand__name">GEARMEND</span>
        <span class="brand__tagline">Motorbike repairs that come to you</span>
      </div>
    </div>
  </section>

  <section class="card card--back" aria-label="Business card back">
    <div class="back__dark">
      <div class="brand">
        <div class="brand__mark"></div>
        <div class="brand__text">
          <span class="brand__name">GEARMEND</span>
          <span class="brand__tagline">Motorbike repairs that come to you</span>
        </div>
      </div>
    </div>
    <div class="back__light">
      <p class="contact__name">Tomas Brandel</p>
      <p class="contact__row">
        <svg class="contact__icon" viewBox="0 0 22 22" aria-hidden="true">
          <rect x="6" y="2" width="10" height="18" rx="2" fill="none" stroke="#141414" stroke-width="1.6"/>
        </svg>
        9312 5827
      </p>
      <p class="contact__row">
        <svg class="contact__icon" viewBox="0 0 22 22" aria-hidden="true">
          <rect x="2" y="5" width="18" height="12" fill="none" stroke="#141414" stroke-width="1.6"/>
          <path d="M2 5 L11 12 L20 5 M2 17 L9 10.5 M20 17 L13 10.5" fill="none" stroke="#141414" stroke-width="1.4"/>
        </svg>
        tomas@gear-mend.com.au
      </p>
    </div>
    <div class="tab tab--right"></div>
    <div class="tab tab--left"></div>
  </section>

</body>
</html>
```